Anzeigengestaltung für Immobilienmakler
Zielgruppe
Wir sind ein Immobilienmakler. Wir wollen eine Plakatkampagne starten. Dazu brauchen wir ein Plakat.
Ich habe noch ein Foto des Plakats hochgeladen, um die Situation zu verdeutlichen.
Aufgabenstellung
Die Maße sind als Anhang dabei. Außerdem dabei ist ein Beispiel eines unserer Werbeschilder (daraus bitte die Farbgebung übernehmen), sowie unser Logo.
Das Plakat sollte mit einem Spruch sein, gerne mit Witz, pfiffig - einfach ein Hingucker.

```html
<!DOCTYPE html>
<html lang="de">
<head>
<meta charset="utf-8">
<title>Plakat – Jonas Bergmann Immobilien</title>
<link rel="stylesheet" href="https://fonts.googleapis.com/css2?family=Roboto+Condensed:wght@700&display=swap">
<style>
  :root {
    --cream: #f6f3ee;
    --sand: #cdbb9d;
    --white: #ffffff;
    --ink: #464646;
    --photo-light: #c9ced3;
    --photo-dark: #4a5560;
  }
  html, body {
    margin: 0;
    padding: 0;
    overflow: hidden;
    background: var(--cream);
  }
  .poster {
    position: relative;
    width: 1200px;
    height: 849px;
    background: var(--cream);
    overflow: hidden;
    font-family: "Roboto Condensed", "Arial Narrow", sans-serif;
  }
  .poster-art {
    position: absolute;
    inset: 0;
  }
  .headline {
    position: absolute;
    left: 440px;
    top: 150px;
    width: 770px;
    margin: 0;
    text-align: center;
    color: var(--ink);
    font-weight: 700;
    font-size: 66px;
    line-height: 99px;
    letter-spacing: -0.5px;
    transform: scaleX(0.93);
  }
  .brand {
    position: absolute;
    left: 518px;
    top: 700px;
    width: 300px;
    text-align: center;
    color: var(--ink);
    font-weight: 700;
    font-size: 26px;
    line-height: 34px;
    letter-spacing: 2px;
  }
  .brand-mark {
    display: block;
    width: 38px;
    height: 38px;
    margin: 0 auto 12px;
    border-radius: 50%;
    background: var(--ink);
  }
</style>
</head>
<body>
<main class="poster">
  <svg class="poster-art" width="1200" height="849" viewBox="0 0 1200 849" aria-hidden="false">
    <defs>
      <linearGradient id="portraitTone" x1="0" y1="0" x2="0.6" y2="1">
        <stop offset="0" stop-color="var(--photo-light)"/>
        <stop offset="0.45" stop-color="#a8adb2"/>
        <stop offset="1" stop-color="var(--photo-dark)"/>
      </linearGradient>
    </defs>

    <!-- sand band behind portrait edge -->
    <path class="portrait-band" fill="var(--sand)"
          d="M0 0 H485 C540 130 575 330 560 520 C548 650 505 760 440 849 H0 Z"/>
    <!-- portrait area -->
    <path class="portrait" role="img" aria-label="Porträtfoto des Immobilienmaklers mit Brille, weißem Hemd und grauem Sakko, lächelnd"
          fill="url(#portraitTone)"
          d="M0 0 H465 C520 130 552 330 538 520 C526 650 485 760 420 849 H0 Z"/>

    <!-- speech bubble shadow -->
    <g class="bubble-shadow" fill="var(--sand)" transform="translate(6 12)">
      <ellipse cx="802" cy="342" rx="400" ry="278"/>
      <path d="M1010 560 L1135 648 L1080 520 Z"/>
    </g>
    <!-- speech bubble -->
    <g class="bubble" fill="var(--white)">
      <ellipse cx="802" cy="342" rx="400" ry="278"/>
      <path d="M1000 560 L1133 645 L1075 515 Z"/>
    </g>
  </svg>

  <h1 class="headline">Er bringt Sie ins<br>Eigenheim, bevor Ihre<br>Schwiegermutter zu<br>Besuch kommt!</h1>

  <div class="brand">
    <span class="brand-mark"></span>
    JONAS BERGMANN<br>IMMOBILIEN
  </div>
</main>
</body>
</html>
```